Fahrzeugbeschriftung: Heizung - Sanitär
Zielgruppe
Wir sind ein junger Meisterbetrieb der Heizungs- und Sanitärbranche und im Rhein-Main-Gebiet für unsere Kunden im Einsatz.
Wir benötigen eine Fahrzeugbeschriftung, die auffällig und modern, jedoch nicht zu verspielt und bunt ist.
Die Beschriftung soll für einen weißen Brava M3 Kasten sein. Es sollten alle Seiten des Fahrzeugs beschriftet werden.
Aufgabenstellung
Die Farbgebung sollte sich am dem Farben des Logos orientieren. Das Firmenlogo sollte im Vordergrund stehen. Auch die Worte Heizung, Sanitär, Solar sollten hervorstechen und gut erkennbar sein. Zusätzlich sollte der Begriff Meisterbetrieb verwendet werden.

```html
<!DOCTYPE html>
<html lang="de">
<head>
<meta charset="utf-8">
<title>HALDEN Haustechnik – Fahrzeugbeschriftung</title>
<link rel="stylesheet" href="https://fonts.googleapis.com/css2?family=Montserrat:wght@700;800&display=swap">
<style>
  :root {
    --navy: #0b2f57;
    --teal: #238592;
    --white: #ffffff;
    --ground: #ffffff;
    --body-light: #f4f5f6;
    --body-shade: #d9dbde;
  }
  html, body {
    margin: 0;
    padding: 0;
    width: 1200px;
    height: 1181px;
    overflow: hidden;
    background: var(--ground);
  }
  .livery {
    display: block;
    width: 1200px;
    height: 1181px;
    font-family: "Montserrat", Arial, sans-serif;
  }
  .vehicle-body { fill: url(#bodyTone); }
  .services { fill: var(--navy); font-weight: 700; font-size: 36px; }
  .company-name { fill: var(--navy); font-weight: 800; font-size: 78px; }
  .company-trade { fill: var(--teal); font-weight: 700; font-size: 36px; }
  .brand-mark-name { fill: var(--navy); font-weight: 800; font-size: 56px; }
  .brand-mark-square { fill: var(--teal); }
  .sill-band { fill: var(--navy); }
  .web-address { fill: var(--white); font-weight: 700; font-size: 21px; }
</style>
</head>
<body>
<svg class="livery" viewBox="0 0 1200 1181" xmlns="http://www.w3.org/2000/svg" aria-label="Fahrzeugbeschriftung HALDEN Haustechnik, linke und rechte Fahrzeugseite">
  <defs>
    <linearGradient id="bodyTone" x1="0" y1="0" x2="0" y2="1">
      <stop offset="0" stop-color="var(--body-light)"/>
      <stop offset="1" stop-color="var(--body-shade)"/>
    </linearGradient>
  </defs>

  <!-- Fahrerseite -->
  <g class="side side-driver">
    <rect class="vehicle-body" x="38" y="135" width="1116" height="420" rx="60" role="img" aria-label="Weißer Kastenwagen, Seitenansicht Fahrerseite"/>

    <text class="services" x="530" y="195" textLength="220" lengthAdjust="spacing">• Heizung</text>
    <text class="services" x="530" y="238" textLength="200" lengthAdjust="spacing">• Sanitär</text>
    <text class="services" x="530" y="281" textLength="150" lengthAdjust="spacing">• Solar</text>

    <g class="brand-mark">
      <rect class="brand-mark-square" x="838" y="255" width="26" height="26"/>
      <text class="brand-mark-name" x="876" y="281">HALDEN</text>
    </g>

    <text class="company-name" x="331" y="396" textLength="408" lengthAdjust="spacing">HALDEN</text>
    <text class="company-trade" x="332" y="436" textLength="406" lengthAdjust="spacing">Haustechnik</text>

    <path class="sill-band" d="M304 456 L872 446 L866 492 L310 498 Z"/>
    <path class="sill-band" d="M1036 436 L1150 434 Q1156 436 1154 452 Q1152 470 1140 472 L1044 482 Z"/>
    <text class="web-address" x="342" y="479" textLength="498" lengthAdjust="spacing">www.halden-haustechnik.de</text>
  </g>

  <!-- Beifahrerseite -->
  <g class="side side-passenger">
    <rect class="vehicle-body" x="43" y="673" width="1117" height="360" rx="60" role="img" aria-label="Weißer Kastenwagen, Seitenansicht Beifahrerseite"/>

    <text class="services" x="456" y="734" textLength="222" lengthAdjust="spacing">• Heizung</text>
    <text class="services" x="456" y="776" textLength="200" lengthAdjust="spacing">• Sanitär</text>
    <text class="services" x="456" y="819" textLength="150" lengthAdjust="spacing">• Solar</text>

    <g class="brand-mark">
      <rect class="brand-mark-square" x="112" y="790" width="26" height="26"/>
      <text class="brand-mark-name" x="150" y="816">HALDEN</text>
    </g>

    <text class="company-name" x="458" y="931" textLength="408" lengthAdjust="spacing">HALDEN</text>
    <text class="company-trade" x="459" y="971" textLength="406" lengthAdjust="spacing">Haustechnik</text>

    <path class="sill-band" d="M52 972 L170 976 L172 1022 L58 1016 Q44 1012 46 996 Q48 974 52 972 Z"/>
    <path class="sill-band" d="M326 982 L896 990 L892 1032 L332 1028 Z"/>
    <text class="web-address" x="357" y="1017" textLength="498" lengthAdjust="spacing">www.halden-haustechnik.de</text>
  </g>
</svg>
</body>
</html>
```